Business Card Design

I need a new business card design for myself. I am a life coach and therapist with both a private practice and now a newly formed business see both my websites: I am looking for a business card to support this and be close to the colours and design of my private practice website and my business website. I am looking for strong bright nature based colours. Sun, Sea and Greenery. The card should reflect inspiration, enlightenment, empowerment and strength!!!
www.helenaroseharwick.com and
www.clear-paths-mentoring.co.uk
Updates
Thank you everyone for your designs. I will be making a final decision by the end of this week and will notify you as soon as possible after this.
Industry/Entity Type
Business
Contact Information for Business Card
Helena Rose Harwick, BSc, PGDip & MRes
Therapist and Life Coach
Clear Paths Mentoring
17 Wexley Road
Manchester
M4 7QT
0800 0619482 Mobile: 07738264917
email: hrharwick@helenaroseharwick.com
Requirements
Must have
- not too busy. To be clear and easy to read information..
and to include this tag line:
"helping you live your life with passion and confidence"

```html
<!DOCTYPE html>
<html lang="en">
<head>
<meta charset="utf-8">
<title>Helena Rose Harwick – Business Card</title>
<link rel="stylesheet" href="https://fonts.googleapis.com/css2?family=Montserrat:wght@400;700&display=swap">
<style>
  :root {
    --backdrop: #e9eaeb;
    --card-white: #ffffff;
    --sun: #f4cf3c;
    --green-light: #a6d66c;
    --green-mid: #5fb84a;
    --green-deep: #3f9f52;
    --sea: #2a96c4;
    --stripe: #fbeaa0;
    --text-green: #4fae47;
    --text-sea: #2a88b4;
  }
  * { margin: 0; padding: 0; box-sizing: border-box; }
  html, body {
    width: 1200px; height: 800px; overflow: hidden;
    background: var(--backdrop);
    font-family: "Montserrat", Arial, sans-serif;
  }
  .sheet {
    width: 1200px; height: 800px;
    display: flex; align-items: center; justify-content: center; gap: 40px;
  }
  .card {
    position: relative;
    width: 540px; height: 309px;
    background: var(--card-white);
    box-shadow: 0 6px 18px rgba(0,0,0,0.12);
    overflow: hidden;
  }
  .card-art { position: absolute; inset: 0; width: 100%; height: 100%; }

  /* Contact side */
  .contact-block {
    position: absolute; left: 205px; top: 32px; right: 16px;
    color: var(--text-green);
  }
  .contact-name { font-size: 21px; font-weight: 700; line-height: 1.1; }
  .contact-role { font-size: 10.5px; font-weight: 400; line-height: 1.3; margin-top: 4px; }
  .contact-row {
    display: flex; align-items: flex-start; gap: 14px;
    font-size: 13.5px; line-height: 1.2; margin-top: 16px;
  }
  .contact-row svg { flex: none; width: 14px; height: 14px; margin-top: 1px; }
  .contact-row.address svg { margin-top: 16px; }
  .contact-row.email { color: var(--text-sea); }

  /* Name side */
  .front-name {
    position: absolute; left: 40px; bottom: 66px;
    color: var(--text-green);
    font-size: 30px; font-weight: 700; letter-spacing: 0.2px;
  }
  .front-tagline {
    position: absolute; left: 40px; bottom: 42px;
    color: var(--text-sea);
    font-size: 13px; font-weight: 400;
  }
</style>
</head>
<body>
<main class="sheet">

  <section class="card card-contact">
    <svg class="card-art" viewBox="0 0 540 309" preserveAspectRatio="none" aria-hidden="true">
      <defs>
        <linearGradient id="swoosh-left" x1="0" y1="0" x2="0.8" y2="1">
          <stop offset="0" stop-color="var(--sun)"/>
          <stop offset="0.3" stop-color="var(--green-light)"/>
          <stop offset="0.65" stop-color="var(--green-mid)"/>
          <stop offset="1" stop-color="var(--sea)"/>
        </linearGradient>
      </defs>
      <path d="M0 0 H175 C125 70 120 200 185 309 H0 Z" fill="url(#swoosh-left)"/>
      <path d="M85 0 C72 120 92 230 158 309" fill="none" stroke="var(--stripe)" stroke-width="3" opacity="0.85"/>
    </svg>
    <div class="contact-block">
      <p class="contact-name">Helena Rose Harwick,</p>
      <p class="contact-role">BSc, PGDip &amp; MRes Therapist and<br>Life Coach Clear Paths Mentoring</p>
      <div class="contact-row address">
        <svg viewBox="0 0 14 14"><path d="M7 1 A4.5 4.5 0 0 1 11.5 5.5 C11.5 8.5 7 13 7 13 C7 13 2.5 8.5 2.5 5.5 A4.5 4.5 0 0 1 7 1 Z" fill="var(--text-green)"/><circle cx="7" cy="5.5" r="1.7" fill="var(--card-white)"/></svg>
        <p>17 Wexley Road<br>Manchester<br>M4 7QT 0800 0619482</p>
      </div>
      <div class="contact-row mobile">
        <svg viewBox="0 0 14 14"><rect x="1.5" y="1.5" width="11" height="11" fill="none" stroke="var(--text-green)" stroke-width="1.3"/></svg>
        <p>07738264917</p>
      </div>
      <div class="contact-row email">
        <svg viewBox="0 0 14 14"><rect x="1" y="3" width="12" height="8.5" fill="none" stroke="var(--text-sea)" stroke-width="1.3"/><path d="M1.5 3.5 L7 8 L12.5 3.5" fill="none" stroke="var(--text-sea)" stroke-width="1.3"/></svg>
        <p>hrharwick@helenaroseharwick.com</p>
      </div>
    </div>
  </section>

  <section class="card card-front">
    <svg class="card-art" viewBox="0 0 540 309" preserveAspectRatio="none" aria-hidden="true">
      <defs>
        <linearGradient id="swoosh-right" x1="0" y1="0" x2="0.6" y2="1">
          <stop offset="0" stop-color="var(--sun)"/>
          <stop offset="0.3" stop-color="var(--green-light)"/>
          <stop offset="0.65" stop-color="var(--green-mid)"/>
          <stop offset="1" stop-color="var(--sea)"/>
        </linearGradient>
      </defs>
      <path d="M320 0 H540 V309 H470 C460 190 430 70 320 0 Z" fill="url(#swoosh-right)"/>
      <path d="M370 0 C440 60 495 170 525 309" fill="none" stroke="var(--stripe)" stroke-width="3" opacity="0.85"/>
    </svg>
    <h1 class="front-name">Helena Rose Harwick</h1>
    <p class="front-tagline">helping you live your life with passion and confidence</p>
  </section>

</main>
</body>
</html>
```